Room 4 Keeps Storage Poster Ad

Room 4 Keeps Storage needs an 8.5" X 11" specialty storage products poster.

Graphics that illustrate seasonal tire storage, bicycle storage, and motorcycle storage.

Information on the poster will be as follows:

Tire storage: $99.00/season + tax
bicycle storage: $99.00/season + tax
motorcycle storage: $250.00/season + tax
Phone: 306-517-4832
Web: www.room4keeps.ca
Address: Room 4 Keeps Storage, 4178 Draven Avenue, Saskatoon, SK, S7M 2R4

**Information does not need to be presented in this exact format. The designer can creatively list the services and the prices. The words phone, web, and address can be left out**

**The season that the ad is targeting is winter

Industry/Entity Type

Storage

```html
<!DOCTYPE html>
<html lang="en">
<head>
<meta charset="utf-8">
<title>Room 4 Keeps Storage – Speciality Storage</title>
<link href="https://fonts.googleapis.com/css2?family=Jost:wght@500;600&family=Montserrat:wght@600;800&display=swap" rel="stylesheet">
<style>
  :root {
    --paper: #ffffff;
    --ink: #111111;
    --band-tire: #464646;
    --band-bicycle: #343434;
    --band-moto: #1e1e1e;
    --band-speciality: #0d0d0d;
    --text-light: #f4f4f4;
    --brand-red: #d32027;
  }
  html, body { margin: 0; padding: 0; overflow: hidden; background: var(--paper); }
  .poster {
    position: relative; width: 900px; height: 1200px; overflow: hidden;
    background: var(--paper); font-family: "Jost", sans-serif; color: var(--text-light);
  }
  .band { position: absolute; top: 0; }
  .band--tire { left: 11px; width: 198px; height: 632px; background: var(--band-tire); }
  .band--bicycle { left: 232px; width: 225px; height: 972px; background: var(--band-bicycle); }
  .band--moto { left: 482px; width: 263px; height: 1050px; background: var(--band-moto); }
  .band--speciality { left: 768px; width: 132px; height: 1200px; background: var(--band-speciality); }

  .vtitle {
    position: absolute; transform-origin: 0 0;
    line-height: 1; white-space: nowrap; font-weight: 500; margin: 0;
    color: var(--text-light);
  }
  .vtitle--tire { left: 35px; top: 275px; font-size: 128px; transform: rotate(-90deg); }
  .vtitle--bicycle { left: 276px; top: 465px; font-size: 120px; transform: rotate(-90deg) scaleX(0.85); }
  .vtitle--motor { left: 513px; top: 450px; font-size: 116px; letter-spacing: 2px; transform: rotate(-90deg) scaleX(0.98); }
  .vtitle--cycle { left: 626px; top: 368px; font-size: 110px; letter-spacing: 2px; transform: rotate(-90deg); }
  .vtitle--speciality { left: 771px; top: 1180px; font-size: 119px; transform: rotate(-90deg) scaleX(0.9); }

  .graphic {
    position: absolute; border-radius: 12px;
    background: radial-gradient(circle at 50% 50%, #8a8a8a 0%, #5a5a5a 100%);
    opacity: .55;
  }
  .graphic--tire { left: 42px; top: 300px; width: 138px; height: 190px; }
  .graphic--bicycle { left: 262px; top: 495px; width: 170px; height: 360px; }
  .graphic--moto { left: 510px; top: 500px; width: 200px; height: 395px; }

  .price {
    position: absolute; display: flex; align-items: flex-start;
    font-family: "Jost", sans-serif; font-weight: 500; color: var(--text-light); line-height: 1;
  }
  .price__amount { font-size: 66px; letter-spacing: -1px; }
  .price__detail { display: flex; flex-direction: column; padding-top: 6px; }
  .price__cents { font-size: 34px; }
  .price__unit { font-size: 15px; letter-spacing: .5px; margin-top: 2px; }
  .price__tax { font-size: 15px; text-align: right; letter-spacing: .5px; margin-top: 2px; }
  .price--tire { left: 15px; top: 545px; }
  .price--bicycle { left: 237px; top: 880px; }
  .price--moto { left: 491px; top: 955px; }

  .brand { position: absolute; left: 20px; top: 1030px; width: 190px; color: var(--ink); }
  .brand__name {
    display: flex; align-items: center; gap: 8px;
    font-family: "Montserrat", sans-serif; font-weight: 800; font-size: 17px;
    line-height: 1.1; color: var(--brand-red); text-transform: uppercase;
    padding-bottom: 10px; border-bottom: 2px solid var(--ink); margin-bottom: 8px;
  }
  .brand__mark { width: 34px; height: 34px; background: var(--brand-red); flex: none; }
  .brand__address {
    font-family: "Montserrat", sans-serif; font-weight: 600; font-size: 11.5px;
    line-height: 1.35; text-transform: uppercase; margin: 0; font-style: normal;
  }
  .contact { position: absolute; left: 240px; top: 1090px; color: var(--ink); font-family: "Montserrat", sans-serif; font-weight: 800; }
  .contact__phone { font-size: 34px; letter-spacing: 13px; line-height: 1; margin: 0 0 14px; }
  .contact__web { font-size: 33px; letter-spacing: 1px; line-height: 1; margin: 0; }
</style>
</head>
<body>
<main class="poster">
  <section class="band band--tire"></section>
  <section class="band band--bicycle"></section>
  <section class="band band--moto"></section>
  <section class="band band--speciality"></section>

  <h2 class="vtitle vtitle--tire">TIRE</h2>
  <h2 class="vtitle vtitle--bicycle">BICYCLE</h2>
  <h2 class="vtitle vtitle--motor">MOTOR</h2>
  <h2 class="vtitle vtitle--cycle">CYCLE</h2>
  <h1 class="vtitle vtitle--speciality">SPECIALITY STORAGE</h1>

  <div class="graphic graphic--tire" role="img" aria-label="Icon of a stack of tires"></div>
  <div class="graphic graphic--bicycle" role="img" aria-label="Icon of a bicycle"></div>
  <div class="graphic graphic--moto" role="img" aria-label="Icon of a motorcycle"></div>

  <div class="price price--tire">
    <span class="price__amount">$99</span>
    <span class="price__detail"><span class="price__cents">.00</span><span class="price__unit">/SEASON</span><span class="price__tax">+ TAX</span></span>
  </div>
  <div class="price price--bicycle">
    <span class="price__amount">$99</span>
    <span class="price__detail"><span class="price__cents">.00</span><span class="price__unit">/SEASON</span><span class="price__tax">+ TAX</span></span>
  </div>
  <div class="price price--moto">
    <span class="price__amount">$250</span>
    <span class="price__detail"><span class="price__cents">.00</span><span class="price__unit">/SEASON</span><span class="price__tax">+ TAX</span></span>
  </div>

  <div class="brand">
    <div class="brand__name"><span class="brand__mark"></span><span>Room 4 Keeps<br>Storage</span></div>
    <address class="brand__address">4178 Draven Avenue,<br>Saskatoon, SK, S7M 2R4</address>
  </div>

  <div class="contact">
    <p class="contact__phone">306-517-4832</p>
    <p class="contact__web">www.room4keeps.ca</p>
  </div>
</main>
</body>
</html>
```